Stationery design for software development / consultancy company

We need stationary design based on company logo.

We are based in London, UK and we are providing integration solutions development / consultancy services for QVR integration projects across UK.

Our name refers two words - integration and grace - and it shows our clients our main specialization field and key characteristics of our solutions / products. We also would like to be associated with follow words: smart, reliable, unique.

Project delivery should include:
- Powerpoint template (needs to have a Cover Page, Table of Contents, 1-2 sample pages, and a Closing/Summary slide at the end)
- Letterhead A4 (Word template)
- Standard invoice A4 (Word template)
- With Compliments Slips A5 (Word template)
- Business card (adobe illustrator)

Attached is logo in vector (please use logo with white background!) and company details for printed stationery.

Target Market(s)

highly skilled IT professionals

Industry/Entity Type

Software

Requirements
Must have
• Clear background in all A4/A5 documents.
All text should be editable, i.e. I will need sources.
Nice to have
• I would prefer light, web 2.0 style colours, follow are in my main interest:
- combination of light grey and orange
- Logo colours
Should not have
• Please no watermarks on printed stationary

```html
<!DOCTYPE html>
<html lang="en">
<head>
<meta charset="utf-8">
<title>Unifold Stationery</title>
<link href="https://fonts.googleapis.com/css2?family=Open+Sans:wght@400;600;700&family=Tinos&display=swap" rel="stylesheet">
<style>
  :root {
    --backdrop: #474747;
    --paper: #ffffff;
    --orange: #fbab3f;
    --ink: #4a4a4a;
    --ink-soft: #6b6b6b;
    --white: #ffffff;
  }
  * { box-sizing: border-box; margin: 0; padding: 0; }
  html, body { width: 1200px; height: 900px; overflow: hidden; }
  body {
    background: var(--backdrop);
    position: relative;
    font-family: "Open Sans", Arial, sans-serif;
    color: var(--ink);
  }

  .brand {
    display: flex;
    align-items: center;
    gap: 8px;
    font-family: "Open Sans", Arial, sans-serif;
    font-weight: 600;
    color: var(--ink);
    line-height: 1;
  }
  .brand-dot {
    border-radius: 50%;
    background: var(--orange);
    flex: none;
  }

  .contact {
    text-align: right;
    font-size: 9px;
    line-height: 16px;
    color: var(--ink-soft);
  }

  .company-details {
    position: absolute;
    left: 0; right: 0;
    text-align: center;
    font-family: "Tinos", "Times New Roman", serif;
    line-height: 14px;
  }

  /* Letterhead */
  .letterhead {
    position: absolute;
    left: 26px; top: 40px;
    width: 554px; height: 776px;
    background: var(--paper);
    overflow: hidden;
  }
  .letterhead-topbar {
    position: absolute; left: 0; top: 0;
    width: 100%; height: 22px;
    background: var(--orange);
  }
  .letterhead .brand {
    position: absolute; right: 22px; top: 38px;
    font-size: 30px;
  }
  .letterhead .brand-dot { width: 22px; height: 22px; }
  .letterhead .contact {
    position: absolute; right: 22px; top: 128px;
  }
  .letterhead-footband {
    position: absolute; left: 0; bottom: 0;
    width: 100%; height: 94px;
  }
  .letterhead .company-details {
    top: 734px;
    color: var(--white);
    font-size: 11px;
    padding-left: 60px;
  }
  .letterhead .company-name { font-family: "Open Sans", Arial, sans-serif; font-size: 9px; }
  .letterhead .company-reg { font-size: 7px; opacity: .85; margin-top: 2px; }

  /* Compliments slip */
  .compliments-slip {
    position: absolute;
    left: 642px; top: 524px;
    width: 550px; height: 242px;
    background: var(--paper);
    overflow: hidden;
  }
  .slip-band {
    position: absolute; left: 0; top: 0;
    width: 550px; height: 70px;
  }
  .slip-title {
    position: absolute; left: 22px; top: 18px;
    font-size: 11px; font-weight: 700;
    letter-spacing: .5px;
    color: var(--white);
  }
  .compliments-slip .brand {
    position: absolute; right: 46px; top: 12px;
    font-size: 26px;
  }
  .compliments-slip .brand-dot { width: 18px; height: 18px; }
  .compliments-slip .contact {
    position: absolute; right: 46px; top: 48px;
  }
  .compliments-slip .company-details {
    top: 192px;
    color: var(--ink);
    font-size: 11px;
  }
  .compliments-slip .company-name { font-size: 10px; color: var(--ink-soft); }
</style>
</head>
<body>

  <section class="letterhead">
    <div class="letterhead-topbar"></div>
    <div class="brand"><span class="brand-dot"></span>unifold</div>
    <div class="contact">
      <p>Tel : +44(0)161 402 7730</p>
      <p>Email : enquiries@unifold.co.uk</p>
      <p>Web : www.unifold.co.uk</p>
    </div>
    <svg class="letterhead-footband" viewBox="0 0 554 94" preserveAspectRatio="none" aria-hidden="true">
      <polygon points="0,32 554,0 554,94 0,94" fill="var(--orange)"/>
    </svg>
    <div class="company-details">
      <p class="company-name">Unifold Limited</p>
      <p>48 Elm Court, 92 Lower Mortlake Road, London</p>
      <p>SW14 8QR, United Kingdom</p>
      <p class="company-reg">Registered in England and Wales No. 08412277 · VAT No. 184 5521 09</p>
    </div>
  </section>

  <section class="compliments-slip">
    <svg class="slip-band" viewBox="0 0 550 70" aria-hidden="true">
      <polygon points="0,0 550,0 550,8 0,64" fill="var(--orange)"/>
    </svg>
    <p class="slip-title">WITH COMPLIMENTS</p>
    <div class="brand"><span class="brand-dot"></span>unifold</div>
    <div class="contact">
      <p>Tel : +44(0)161 402 7730</p>
      <p>Email : enquiries@unifold.co.uk</p>
      <p>Web : www.unifold.co.uk</p>
    </div>
    <div class="company-details">
      <p class="company-name">Unifold Limited</p>
      <p>48 Elm Court, 92 Lower Mortlake Road, London</p>
      <p>SW14 8QR, United Kingdom</p>
    </div>
  </section>

</body>
</html>
```